Improve and Enhance existing design. Roast and Chips

We are an Operations Management company working with cafes, convenience stores, and petrol stations to improve their marketing.

The design work I have for you is to improve, enhance and make ready for hi res printing (with crop marks) in A1 A3 and A4. The attached is the concept and content.

I would like to see examples based on the attached offer.

Thank you.

Bev

```html
<!DOCTYPE html>
<html lang="en">
<head>
<meta charset="utf-8">
<title>Roast Roll &amp; Chips – $8 Only</title>
<link rel="stylesheet" href="https://fonts.googleapis.com/css2?family=Sorts+Mill+Goudy&family=Roboto:wght@900&display=swap">
<style>
  :root {
    --frame-dark: #6f1d15;
    --frame-mid: #a5271f;
    --card: #ffffff;
    --ink: #7b2b1f;
    --tag-gold: #f6c21a;
    --tag-edge: #e39a12;
    --tag-brown: #7a2a1c;
    --string: #8a8a8a;
    --price: #ffffff;
    --meal-warm: #dfa55a;
    --meal-mid: #ecc98c;
    --meal-plate: #f4ece0;
  }
  * { margin: 0; padding: 0; box-sizing: border-box; }
  html, body { width: 843px; height: 1200px; overflow: hidden; }
  body {
    position: relative;
    background: radial-gradient(ellipse at 50% 50%, var(--frame-mid) 55%, var(--frame-dark) 100%);
    font-family: "Sorts Mill Goudy", "Goudy Old Style", Georgia, serif;
  }
  .poster-card {
    position: absolute;
    left: 38px; top: 53px;
    width: 767px; height: 1092px;
    background: var(--card);
    border-radius: 31px;
  }
  .headline { font-weight: 400; }
  .headline span {
    position: absolute;
    color: var(--ink);
    line-height: 1;
    white-space: nowrap;
  }
  .headline .ampersand { left: 112px; top: 200px; font-size: 290px; }
  .headline .line-roast { left: 260px; top: 238px; font-size: 70px; letter-spacing: 1px; }
  .headline .line-chips { left: 344px; top: 326px; font-size: 121px; letter-spacing: 1px; }
  .offer-only { position: absolute; left: 424px; top: 506px; font-size: 102px; color: var(--ink); line-height: 1; letter-spacing: 2px; }
  .tag-string { position: absolute; left: 0; top: 0; width: 843px; height: 1200px; pointer-events: none; }
  .price-tag { position: absolute; left: 204px; top: 442px; width: 196px; height: 196px; }
  .price-tag .price {
    font-family: "Roboto", Arial, sans-serif;
    font-weight: 900;
    font-size: 92px;
    fill: var(--price);
  }
  .meal-photo {
    position: absolute;
    left: 100px; top: 748px;
    width: 584px; height: 336px;
    border-radius: 22px;
    background: linear-gradient(180deg, var(--meal-warm) 0%, var(--meal-mid) 55%, var(--meal-plate) 100%);
  }
</style>
</head>
<body>
  <div class="poster-card"></div>

  <h1 class="headline">
    <span class="ampersand" aria-hidden="true">&amp;</span>
    <span class="line-roast">ROAST ROLL</span>
    <span class="line-chips">CHIPS</span>
  </h1>

  <svg class="tag-string" viewBox="0 0 843 1200" aria-hidden="true">
    <path d="M302,472 C292,440 272,412 268,394 C265,380 280,376 287,392 C294,410 300,440 302,472"
          fill="none" stroke="var(--string)" stroke-width="2.5" stroke-linecap="round"/>
  </svg>

  <svg class="price-tag" viewBox="-98 -98 196 196" role="img" aria-label="$8 price tag">
    <defs>
      <polygon id="octagon" points="98,0 69.3,69.3 0,98 -69.3,69.3 -98,0 -69.3,-69.3 0,-98 69.3,-69.3"/>
    </defs>
    <g fill="var(--tag-gold)">
      <use href="#octagon"/>
      <use href="#octagon" transform="rotate(9)"/>
      <use href="#octagon" transform="rotate(18)"/>
      <use href="#octagon" transform="rotate(27)"/>
      <use href="#octagon" transform="rotate(36)"/>
    </g>
    <circle r="84" fill="none" stroke="var(--tag-edge)" stroke-width="2"/>
    <circle r="80" fill="var(--tag-brown)"/>
    <circle cx="0" cy="-68" r="6" fill="var(--card)" stroke="var(--string)" stroke-width="1.5"/>
    <text class="price" x="0" y="33" text-anchor="middle">$8</text>
  </svg>

  <div class="offer-only">ONLY</div>

  <div class="meal-photo" role="img" aria-label="Photo of a burger roll with lettuce and tomato, fries and a small dish of tomato sauce on a white plate"></div>
</body>
</html>
```